Bref créative
Valtoni Building and Design Stationary
Valtoni Building & Design
Professional
Martin K. Valtoni
President / Owner
4172 Wexmoor Avenue
Suite 2807
Kestrel Point, KP 07319
mkvaltoni@valtonibuilding.example
www.valtonibuilding.example
The logo, which will be uploaded.
Logo for the back of card. Please show us versions with both black background and white background.
Logo with white background. Please show us versions for back of card with both black and white background.

```html
<!DOCTYPE html>
<html lang="en">
<head>
<meta charset="utf-8">
<title>Valtoni Building &amp; Design — Business Cards</title>
<link rel="stylesheet" href="https://fonts.googleapis.com/css2?family=Roboto:wght@400;500&family=Marcellus+SC&display=swap">
<style>
  :root {
    --backdrop: #e9e2d8;
    --red-hot: #f0463c;
    --red-deep: #8c2a22;
    --red-mark: #b8322a;
    --ink-dark: #151515;
    --paper: #ffffff;
    --swoosh: #9a9a9a;
    --label: #3a3330;
    --text-light: #ffffff;
  }
  * { box-sizing: border-box; margin: 0; padding: 0; }
  html, body { width: 1200px; height: 821px; overflow: hidden; }
  body {
    background: var(--backdrop);
    font-family: "Roboto", Arial, sans-serif;
    position: relative;
  }
  .card {
    position: absolute;
    width: 511px;
    height: 281px;
    border-radius: 18px;
    overflow: hidden;
    box-shadow: 0 4px 10px rgba(0,0,0,0.25);
  }
  .card-shape { position: absolute; inset: 0; width: 100%; height: 100%; }
  .front-a { left: 65px; top: 43px; }
  .front-b { left: 619px; top: 43px; }
  .back-dark { left: 65px; top: 427px; background: var(--ink-dark); }
  .back-light { left: 619px; top: 427px; background: var(--paper); }

  .holder { position: absolute; left: 24px; top: 20px; color: var(--text-light); }
  .holder-name { font-size: 14px; font-weight: 400; }
  .holder-title { font-size: 9px; margin-top: 5px; opacity: 0.9; }

  .contact { position: absolute; left: 24px; bottom: 18px; color: var(--text-light); font-size: 8.5px; list-style: none; }
  .contact li { display: flex; align-items: flex-start; gap: 7px; line-height: 12px; margin-top: 3px; }
  .contact svg { width: 9px; height: 9px; margin-top: 2px; flex: none; fill: var(--text-light); }

  .mark {
    position: absolute;
    text-align: center;
    color: var(--red-mark);
    font-weight: 500;
    line-height: 1.05;
  }
  .mark-word { display: block; font-size: 32px; }
  .mark-sub { display: block; font-size: 10.5px; letter-spacing: 0.5px; margin-top: 4px; white-space: nowrap; }
  .front-a .mark, .front-b .mark { right: 14px; top: 92px; width: 136px; }
  .back-dark .mark, .back-light .mark { left: 0; right: 0; top: 100px; }
  .back-dark .mark-word, .back-light .mark-word { font-size: 44px; }
  .back-dark .mark-sub, .back-light .mark-sub { font-size: 14px; letter-spacing: 1px; }

  .label {
    position: absolute;
    width: 511px;
    text-align: center;
    font-family: "Marcellus SC", Georgia, serif;
    font-size: 20px;
    letter-spacing: 2.5px;
    color: var(--label);
  }
</style>
</head>
<body>

  <div class="card front-a">
    <svg class="card-shape" viewBox="0 0 511 281" aria-hidden="true">
      <defs>
        <radialGradient id="red-a" cx="0.3" cy="0.4" r="0.75">
          <stop offset="0" stop-color="var(--red-hot)"/>
          <stop offset="1" stop-color="var(--red-deep)"/>
        </radialGradient>
      </defs>
      <rect width="511" height="281" fill="url(#red-a)"/>
      <path d="M352,0 C322,70 330,120 338,150 C348,195 318,250 298,281" fill="none" stroke="#d9d9d9" stroke-width="6"/>
      <path d="M360,0 C330,70 338,120 346,150 C356,195 326,250 306,281 L511,281 L511,0 Z" fill="var(--ink-dark)"/>
    </svg>
    <div class="holder">
      <p class="holder-name">Martin K. Valtoni</p>
      <p class="holder-title">President / Owner</p>
    </div>
    <ul class="contact">
      <li><svg viewBox="0 0 10 10"><path d="M5 0 10 4.5H8.5V10H1.5V4.5H0Z"/></svg><span>4172 Wexmoor Avenue<br>Suite 2807<br>Kestrel Point, KP 07319</span></li>
      <li><svg viewBox="0 0 10 10"><path d="M2 0h6v10H2z M3 1v7h4V1z"/></svg><span>201-555-0148</span></li>
      <li><svg viewBox="0 0 10 10"><path d="M0 2h10v6H0z"/></svg><span>mkvaltoni@valtonibuilding.example</span></li>
      <li><svg viewBox="0 0 10 10"><circle cx="5" cy="5" r="4.5"/></svg><span>www.valtonibuilding.example</span></li>
    </ul>
    <p class="mark"><span class="mark-word">Valtoni</span><span class="mark-sub">BUILDING &amp; DESIGN</span></p>
  </div>

  <div class="card front-b">
    <svg class="card-shape" viewBox="0 0 511 281" aria-hidden="true">
      <defs>
        <radialGradient id="red-b" cx="0.3" cy="0.4" r="0.75">
          <stop offset="0" stop-color="var(--red-hot)"/>
          <stop offset="1" stop-color="var(--red-deep)"/>
        </radialGradient>
      </defs>
      <rect width="511" height="281" fill="url(#red-b)"/>
      <path d="M352,0 C322,70 330,120 338,150 C348,195 318,250 298,281" fill="none" stroke="var(--swoosh)" stroke-width="7"/>
      <path d="M360,0 C330,70 338,120 346,150 C356,195 326,250 306,281 L511,281 L511,0 Z" fill="var(--paper)"/>
    </svg>
    <div class="holder">
      <p class="holder-name">Martin K. Valtoni</p>
      <p class="holder-title">President / Owner</p>
    </div>
    <ul class="contact">
      <li><svg viewBox="0 0 10 10"><path d="M5 0 10 4.5H8.5V10H1.5V4.5H0Z"/></svg><span>4172 Wexmoor Avenue<br>Suite 2807<br>Kestrel Point, KP 07319</span></li>
      <li><svg viewBox="0 0 10 10"><path d="M2 0h6v10H2z M3 1v7h4V1z"/></svg><span>201-555-0148</span></li>
      <li><svg viewBox="0 0 10 10"><path d="M0 2h10v6H0z"/></svg><span>mkvaltoni@valtonibuilding.example</span></li>
      <li><svg viewBox="0 0 10 10"><circle cx="5" cy="5" r="4.5"/></svg><span>www.valtonibuilding.example</span></li>
    </ul>
    <p class="mark"><span class="mark-word">Valtoni</span><span class="mark-sub">BUILDING &amp; DESIGN</span></p>
  </div>

  <p class="label" style="left:65px; top:364px;">Business Card Option A</p>
  <p class="label" style="left:619px; top:364px;">Business Card Option B</p>

  <div class="card back-dark">
    <p class="mark"><span class="mark-word">Valtoni</span><span class="mark-sub">BUILDING &amp; DESIGN</span></p>
  </div>
  <div class="card back-light">
    <p class="mark"><span class="mark-word">Valtoni</span><span class="mark-sub">BUILDING &amp; DESIGN</span></p>
  </div>

  <p class="label" style="left:65px; top:744px;">Business Card Back</p>
  <p class="label" style="left:619px; top:744px;">Business Card Back</p>

</body>
</html>
```